Arvo 7 Detection Wheel

We need a professional **framework wheel diagram** designed for our detection dog training manual.

Our business is **Arvo 7 Dog Training**, and this graphic represents our **Detection Training Model**.

Please use the **attached reference images** as a guide for the structure and layout of the wheel.

### What we need

1. **Full wheel graphic**

* Clean circular framework wheel
* Similar structure to the attached example
* Clear sections and text
* Professional training manual style
* Transparent background

2. **Individual segment pieces**

We also need the **inner sections broken into separate pieces** (like the second reference image).

This will allow us to place each section on different pages of the manual when explaining the concepts.

Each piece should look like a **slice of the wheel**.

### Style

The design should look:

• Professional
• Clean and modern
• Structured and easy to read
• Suitable for a training manual

Avoid cartoon styles or clipart.

### Colours

Please use our brand colour palette (see attached image):

* Dark navy blue
* Steel blue
* Light blue
* White
* Light grey
* Dark grey

### Files required

Final files must include:

* Vector files (AI or EPS)
* Transparent PNG
* High-resolution PDF

Please also provide **each segment exported individually**

```html
<!DOCTYPE html>
<html lang="en">
<head>
<meta charset="utf-8">
<title>Operational Capabilities Area</title>
<link rel="stylesheet" href="https://fonts.googleapis.com/css2?family=Montserrat:wght@600;700&display=swap">
<style>
  :root {
    --slice-face: #68a5bd;
    --slice-rim: #5395aa;
    --label: #ffffff;
    --title: #111111;
    --paper: #ffffff;
  }
  html, body {
    margin: 0;
    padding: 0;
    width: 1172px;
    height: 1200px;
    overflow: hidden;
    background: var(--paper);
  }
  .wheel-diagram {
    display: block;
    width: 1172px;
    height: 1200px;
  }
  .slice-rim { fill: var(--slice-rim); }
  .slice-face { fill: var(--slice-face); }
  .slice-label {
    font-family: "Montserrat", sans-serif;
    font-weight: 700;
    font-size: 41.5px;
    fill: var(--label);
    text-anchor: middle;
    filter: drop-shadow(3px 3px 2px rgba(0, 0, 0, 0.45));
  }
  .wheel-title {
    font-family: "Montserrat", sans-serif;
    font-weight: 700;
    font-size: 55px;
    fill: var(--title);
    text-anchor: middle;
  }
</style>
</head>
<body>
<svg class="wheel-diagram" viewBox="0 0 1900 1945" xmlns="http://www.w3.org/2000/svg" aria-label="Operational Capabilities Area wheel">
  <g class="slice slice--development">
    <path class="slice-rim" d="M862 720 L325 348 A800 800 0 0 1 636 107 Z"/>
    <path class="slice-face" d="M862 720 L367 376 A750 750 0 0 1 653 155 Z"/>
    <text class="slice-label" x="565" y="378">Development</text>
  </g>
  <g class="slice slice--distractions">
    <path class="slice-rim" d="M1000 810 L773 195 A664 664 0 0 1 1227 195 Z"/>
    <path class="slice-face" d="M1000 810 L790 240 A614 614 0 0 1 1210 240 Z"/>
    <text class="slice-label" x="1000" y="350">Distractions</text>
  </g>
  <g class="slice slice--behaviour">
    <path class="slice-rim" d="M1137 743 L1363 130 A800 800 0 0 1 1675 370 Z"/>
    <path class="slice-face" d="M1137 743 L1348 177 A750 750 0 0 1 1632 400 Z"/>
    <text class="slice-label" x="1428" y="413">Behaviour</text>
  </g>
  <g class="slice slice--handler">
    <path class="slice-rim" d="M1113 870 L1651 498 A800 800 0 0 1 1768 870 Z"/>
    <path class="slice-face" d="M1113 870 L1612 527 A750 750 0 0 1 1718 870 Z"/>
    <text class="slice-label" x="1523" y="770">Handler</text>
  </g>
  <g class="slice slice--search-method">
    <path class="slice-rim" d="M1083 966 L1740 966 A800 800 0 0 1 1547 1430 Z"/>
    <path class="slice-face" d="M1083 966 L1690 966 A750 750 0 0 1 1513 1395 Z"/>
    <text class="slice-label" x="1477" y="1105">Search Method</text>
  </g>
  <g class="slice slice--reinforcement">
    <path class="slice-rim" d="M1083 1098 L1547 1562 A800 800 0 0 1 1083 1754 Z"/>
    <path class="slice-face" d="M1083 1098 L1512 1528 A750 750 0 0 1 1083 1704 Z"/>
    <text class="slice-label" x="1278" y="1506">Reinforcement</text>
  </g>
  <g class="slice slice--deployment">
    <path class="slice-rim" d="M869 1127 L405 1589 A800 800 0 0 0 869 1782 Z"/>
    <path class="slice-face" d="M869 1127 L440 1556 A750 750 0 0 0 869 1732 Z"/>
    <text class="slice-label" x="679" y="1534">Deployment</text>
  </g>
  <g class="slice slice--target-odour">
    <path class="slice-rim" d="M873 952 L409 1416 A800 800 0 0 1 217 952 Z"/>
    <path class="slice-face" d="M873 952 L443 1382 A750 750 0 0 1 267 952 Z"/>
    <text class="slice-label" x="493" y="1092">Target Odour</text>
  </g>
  <g class="slice slice--integrity">
    <path class="slice-rim" d="M807 856 L152 856 A800 800 0 0 1 270 484 Z"/>
    <path class="slice-face" d="M807 856 L202 856 A750 750 0 0 1 307 513 Z"/>
    <text class="slice-label" x="415" y="758">Integrity</text>
  </g>
  <text class="wheel-title" x="1000" y="1868">Operational Capabilities Area</text>
</svg>
</body>
</html>
```